Norvale Email Signature Banners – Fabrication Capability Series

www.Norvale.com.au is an Australian engineering and fabrication company specialising in fabrication and welding of :
steel piping spools,
skids and frames,
small volume process steel tanks
and general steel fabrication
We require four distinct banner designs for use in Teldrin Quillmark email signatures. Each banner will highlight a specific capability while maintaining a consistent brand identity.
Deliverables
Four banners total:
Piping Spools Fabrication – focus on precision welding and stainless steel pipework
Skid & Frames Fabrication – highlight skid systems and structural frames
Small Steel Tanks Fabrication – show fabricated tanks and workshop craftsmanship
General Fabrication Solutions – broad steel fabrication theme for company-wide use
Dimensions: 600–700 px wide × 100 px high
Format: PNG (preferred), small file size prefered
Resolution: 72 dpi
Background: non-transparent, industrial or workshop setting
Text examples:
1. Piping Spools Fabrication
Option A: “Expert Fabrication Solutions for Process Piping”
Option B: “Precision Welding for Complex Systems”
Option C: “Delivering Quality in Every Spool”
Option D: “Engineered for Flow, Built for Strength”
2. Skid & Frames Fabrication
Option A: “Custom Engineered Modular Systems”
Option B: “Built Strong. Designed Smart.”
Option C: “Reliable Frames for Industrial Performance”
Option D: “Modular Fabrication for Seamless Integration”
3. Small Steel Tanks Fabrication
Option A: “Precision Built for Your Needs”
Option B: “Compact Strength. Proven Durability.”
Option C: “Fabricated for Performance and Longevity”
Option D: “Small Tanks. Big Reliability.”
4. General Fabrication Solutions
Option A: “Quality Craftsmanship, Proven Results”
Option B: “Your Partner in Precision Fabrication”
Option C: “Engineering Excellence in Every Weld”
Option D: “Australian Fabrication. Global Standards.”
Style Direction
Clean, professional, and engineering‑focused
Use Norvale brand colours
Blend photo realism with vector clarity (no heavy gradients)
Include subtle industrial textures or workshop imagery
Typography: bold sans‑serif, legible at small scale
Usage Context
These banners will appear at the bottom of staff email signatures via Quillmark Email Signature Tool for Teldrin 365, so clarity and fast loading are essential. No Logo is required in the banners.
Reference
Existing Norvale signature is attached. Colour palette to match the signature style and logo.
Target Market(s)
Engineering and construction companies,
Industry/Entity Type
Engineering fabrication design

```html
<!DOCTYPE html>
<html lang="en">
<head>
<meta charset="utf-8">
<title>Norvale Email Signature Banners</title>
<link rel="stylesheet" href="https://fonts.googleapis.com/css2?family=Poppins:ital,wght@0,600;1,600&display=swap">
<style>
  :root {
    --canvas-grey: #8c8c8c;
    --panel-dark: #1a1a1a;
    --brand-blue: #29a6e0;
    --photo-deep: #07364f;
    --photo-mid: #0f6f9c;
    --photo-light: #2aa0d6;
    --text-white: #ffffff;
  }
  * { margin: 0; padding: 0; box-sizing: border-box; }
  html, body {
    width: 1200px; height: 876px; overflow: hidden;
    background: var(--canvas-grey);
  }
  .banner-sheet { position: relative; width: 1200px; height: 876px; }
  .banner {
    position: absolute; left: 113px; width: 974px; height: 162px;
  }
  .banner svg { position: absolute; inset: 0; display: block; }
  .banner-copy {
    position: absolute; left: 44px; top: 0; height: 162px;
    display: flex; flex-direction: column; justify-content: center;
    font-family: "Poppins", sans-serif; font-weight: 600;
    font-size: 26px; line-height: 33px; color: var(--text-white);
    letter-spacing: -0.2px;
  }
  .accent {
    color: var(--brand-blue); font-style: italic;
    display: inline-block; position: relative;
  }
  .accent::after {
    content: ""; position: absolute; left: 0; right: -4px; bottom: 1px;
    height: 1px;
    background: linear-gradient(90deg, var(--brand-blue), rgba(41,166,224,0.3));
  }
  .banner--general { top: 82px; }
  .banner--piping  { top: 265px; }
  .banner--tanks   { top: 449px; }
  .banner--skids   { top: 633px; }
</style>
</head>
<body>
<main class="banner-sheet">

  <section class="banner banner--general">
    <svg viewBox="0 0 974 162" width="974" height="162">
      <defs>
        <linearGradient id="photo-general" x1="0" y1="0" x2="1" y2="1">
          <stop offset="0" stop-color="var(--photo-mid)"/>
          <stop offset="0.5" stop-color="var(--photo-light)"/>
          <stop offset="1" stop-color="var(--photo-deep)"/>
        </linearGradient>
      </defs>
      <rect class="panel-dark" width="974" height="162" fill="var(--panel-dark)"/>
      <polygon role="img" aria-label="Steel pipe storage inside a fabrication workshop, blue toned" points="455,0 974,0 974,162 426,162" fill="url(#photo-general)"/>
      <polygon class="slant-stripe" points="452,0 455,0 426,162 411,162" fill="var(--brand-blue)"/>
    </svg>
    <div class="banner-copy">
      <p>Engineering <span class="accent">Excellence</span></p>
      <p>in Every Weld</p>
    </div>
  </section>

  <section class="banner banner--piping">
    <svg viewBox="0 0 974 162" width="974" height="162">
      <defs>
        <radialGradient id="photo-piping" cx="0.45" cy="0.9" r="0.8">
          <stop offset="0" stop-color="#bfe6f7"/>
          <stop offset="0.25" stop-color="var(--photo-light)"/>
          <stop offset="0.7" stop-color="var(--photo-mid)"/>
          <stop offset="1" stop-color="var(--photo-deep)"/>
        </radialGradient>
      </defs>
      <rect class="panel-dark" width="974" height="162" fill="var(--panel-dark)"/>
      <polygon role="img" aria-label="Welder working on pipework with bright sparks, blue toned" points="455,0 974,0 974,162 426,162" fill="url(#photo-piping)"/>
      <polygon class="slant-stripe" points="452,0 455,0 426,162 411,162" fill="var(--brand-blue)"/>
    </svg>
    <div class="banner-copy">
      <p>Expert <span class="accent">Fabrication Solutions</span></p>
      <p>for Process Piping</p>
    </div>
  </section>

  <section class="banner banner--tanks">
    <svg viewBox="0 0 974 162" width="974" height="162">
      <defs>
        <linearGradient id="photo-tanks" x1="0" y1="0" x2="1" y2="0">
          <stop offset="0" stop-color="var(--photo-light)"/>
          <stop offset="0.55" stop-color="var(--photo-mid)"/>
          <stop offset="1" stop-color="var(--photo-deep)"/>
        </linearGradient>
      </defs>
      <rect class="panel-dark" width="974" height="162" fill="var(--panel-dark)"/>
      <polygon role="img" aria-label="Gloved hands measuring steel sections with a caliper, blue toned" points="455,0 974,0 974,162 426,162" fill="url(#photo-tanks)"/>
      <polygon class="slant-stripe" points="452,0 455,0 426,162 411,162" fill="var(--brand-blue)"/>
    </svg>
    <div class="banner-copy">
      <p>Compact Strength</p>
      <p>Proven <span class="accent">Durability</span></p>
    </div>
  </section>

  <section class="banner banner--skids">
    <svg viewBox="0 0 974 162" width="974" height="162">
      <defs>
        <linearGradient id="photo-skids" x1="0" y1="0" x2="1" y2="1">
          <stop offset="0" stop-color="var(--photo-mid)"/>
          <stop offset="0.6" stop-color="var(--photo-light)"/>
          <stop offset="1" stop-color="#4bb8e6"/>
        </linearGradient>
      </defs>
      <rect class="panel-dark" width="974" height="162" fill="var(--panel-dark)"/>
      <polygon role="img" aria-label="Structural steel frame under construction against the sky, blue toned" points="455,0 974,0 974,162 426,162" fill="url(#photo-skids)"/>
      <polygon class="slant-stripe" points="452,0 455,0 426,162 411,162" fill="var(--brand-blue)"/>
    </svg>
    <div class="banner-copy">
      <p>Custom <span class="accent">Engineered</span></p>
      <p>Modular Systems</p>
    </div>
  </section>

</main>
</body>
</html>
```